Web design for business website

I need a web design for a business website for one of our clients who is specialized in alarm management software. I would like you to design 3 web pages, one for each of the 3 pages. You need to process the corporate identity of our client to the web design. This means the colors of the logo (red and black) should definitely show up on all of the 3 pages. Find the logo file for the logo of our customer. To increase readability I suggest you use a white/light background. All suggestions are welcome.

Please kindly download atttached Webdesign.zip and read the project brief first. The project brief refers to all other files of the zip file. Your design must have exactly the same structure as the wireframes.
Updates

Target Market(s)

B2B, Alarm management

Industry/Entity Type

Business

Number of Pages Required

3 page

Requirements
Must have
• The web design must have exactly the same structure as the wireframes and needs to contain the colors of the company logo.

```html
<!DOCTYPE html>
<html lang="en">
<head>
<meta charset="utf-8">
<title>Kelvora – Real-time reasoning solutions</title>
<link href="https://fonts.googleapis.com/css2?family=Arimo:wght@400;700&family=Montserrat:wght@700&display=swap" rel="stylesheet">
<style>
:root{
  --red:#c0391f;
  --ink:#1f1d24;
  --text:#444;
  --muted:#777;
  --top:#e6e6e6;
  --head:#f1f1f1;
  --line:#dcdcdc;
  --foot:#1c1a1b;
  --panel:#232122;
  --white:#fff;
}
*{margin:0;padding:0;box-sizing:border-box}
html,body{width:837px;height:1200px;overflow:hidden}
body{position:relative;background:var(--white);font-family:"Arimo",Arial,sans-serif;color:var(--text)}
.abs{position:absolute}
.topbar{left:0;top:0;width:837px;height:32px;background:var(--top)}
.call{left:69px;top:11px;font-size:9px;font-weight:700;color:var(--ink)}
.lang{left:547px;top:11px;font-size:8.5px;color:var(--ink);display:flex;align-items:center;gap:4px}
.flag{width:11px;height:7px;background:linear-gradient(#2b4a8c,#2b4a8c);border:1px solid #fff;outline:1px solid #c33}
.search{left:623px;top:7px;width:145px;height:19px;background:#fff;border:1px solid #d6d6d6;font-size:7.5px;color:#999;padding:5px 6px}
.header{left:0;top:32px;width:837px;height:120px;background:var(--head)}
.logo{left:69px;top:54px;display:flex;align-items:center;gap:10px}
.logo-dot{width:33px;height:33px;border-radius:50%;background:var(--red)}
.logo-name{font-family:"Montserrat",sans-serif;font-weight:700;font-size:23px;letter-spacing:1.5px;color:var(--ink);line-height:1}
.logo-tag{font-size:7.5px;color:var(--ink);margin-top:2px}
.userbtn{top:51px;width:47px;height:42px;background:#fff;font-size:8px;color:var(--ink);text-align:center;padding-top:7px}
.userbtn svg{display:block;margin:0 auto 4px}
.nav{left:69px;top:111px;width:699px;height:41px;background:var(--red);display:flex;align-items:center;padding-left:22px}
.nav a{color:#fff;text-decoration:none;font-size:8.5px;margin-right:45px;position:relative}
.nav a.on::after{content:"";position:absolute;left:50%;top:20px;margin-left:-3px;border:3px solid transparent;border-top-color:var(--red)}
.hero{left:69px;top:167px;width:700px;height:328px;background:#fff;border:1px solid #ccc;padding:2px;box-shadow:0 10px 12px -8px rgba(0,0,0,.35)}
.hero-photo{width:100%;height:100%;background:linear-gradient(180deg,#c9b79a 0%,#e3b468 35%,#6c6a52 55%,#4f5a3c 72%,#a48a5e 100%)}
.hero-title{left:69px;top:338px;width:700px;text-align:center;color:#fff;font-weight:700;font-size:29px;text-shadow:0 2px 4px rgba(0,0,0,.5)}
.hero-sub{left:69px;top:388px;width:700px;text-align:center;color:#fff;font-weight:700;font-size:16px;text-shadow:0 2px 4px rgba(0,0,0,.5)}
.dots{left:404px;top:475px;display:flex;gap:2px}
.dots i{width:6px;height:6px;border-radius:50%;background:#111}
.dots i:first-child{background:var(--red)}
.dropdown{left:179px;top:169px;width:296px;height:130px;background:#fff}
.dropdown ul{list-style:none;position:absolute;left:8px;top:6px;width:128px}
.dropdown li{font-size:8px;color:#555;padding:8px 0 8px 1px;border-bottom:1px dashed #999}
.dropdown li:last-child{border:0}
.drop-photo{left:152px;top:7px;width:136px;height:82px;background:linear-gradient(135deg,#2f4a6b,#c9a24a 50%,#4d6a55)}
.drop-label{left:151px;top:104px;font-size:11px;font-weight:700;color:var(--red)}
.section-title{left:0;width:837px;text-align:center;font-weight:700;font-size:14.5px;color:var(--ink)}
.rule{left:0;width:837px;height:6px}
.intro{left:80px;top:583px;width:677px;text-align:center;font-size:8.2px;line-height:15.7px;color:var(--text)}
.intro p{margin-bottom:12px}
.divider{left:69px;top:706px;width:699px;height:1px;background:var(--line)}
.clients{left:69px;top:803px;display:flex;gap:22px}
.client{width:82px;height:65px;border:1px solid var(--line);display:flex;align-items:center;justify-content:center;font-size:10px;font-weight:700;color:var(--ink);gap:4px}
.client i{width:9px;height:9px;border-radius:50%;background:var(--red)}
.footer{left:0;top:916px;width:837px;height:284px;background:var(--foot)}
.social{left:69px;top:934px;display:flex;gap:11px}
.social i{width:25px;height:25px;border-radius:50%;background:#2e2c2d}
.email{left:538px;top:937px;width:143px;height:24px;background:#fff;border-radius:2px;font-size:7.5px;color:#888;padding:8px 7px}
.subscribe{left:693px;top:937px;width:75px;height:24px;background:var(--red);color:#fff;font-size:9px;text-align:center;padding-top:7px}
.panel{left:69px;top:980px;width:699px;height:170px;background:var(--panel)}
.col{top:1013px}
.col h4{font-size:10.5px;font-weight:400;color:var(--red);margin-bottom:10px}
.col li{list-style:none;font-size:8px;color:#eee;line-height:18px}
.contact{font-size:8px;color:#eee;line-height:18px;width:108px}
.copy{left:0;top:1169px;width:837px;text-align:center;font-size:7.5px;color:#777}
</style>
</head>
<body>

<div class="abs topbar"></div>
<div class="abs call">CALL US : +31 (0) 20 555 0148</div>
<div class="abs lang"><span class="flag"></span>English ▾</div>
<div class="abs search">Search here...</div>

<div class="abs header"></div>
<div class="abs logo">
  <span class="logo-dot"></span>
  <div><div class="logo-name">KELVORA</div><div class="logo-tag">Real-time reasoning solutions</div></div>
</div>

<div class="abs userbtn" style="left:607px">
  <svg width="14" height="14" viewBox="0 0 14 14"><circle cx="7" cy="4" r="3.2" fill="#333"/><path d="M1 14c0-4 3-6 6-6s6 2 6 6z" fill="#333"/></svg>Account</div>
<div class="abs userbtn" style="left:664px">
  <svg width="14" height="14" viewBox="0 0 14 14"><path d="M4 6V4a3 3 0 0 1 6 0v2" stroke="#333" stroke-width="1.6" fill="none"/><rect x="2.5" y="6" width="9" height="8" fill="#333"/></svg>Login</div>
<div class="abs userbtn" style="left:720px">
  <svg width="14" height="14" viewBox="0 0 14 14"><circle cx="6" cy="4" r="3" fill="#333"/><path d="M0 14c0-4 3-6 6-6s6 2 6 6z" fill="#333"/><path d="M11 1v4M9 3h4" stroke="#333" stroke-width="1.2"/></svg>Signup</div>

<nav class="abs nav">
  <a>HOME</a><a class="on">INDUSTRY</a><a>TELECOM</a><a>POWER</a><a>UTILITIES</a><a>INFRA</a><a>STORE</a>
</nav>

<div class="abs hero"><div class="hero-photo" role="img" aria-label="Refinery at sunset reflected in marshland water"></div></div>
<div class="abs hero-title">KELVORA</div>
<div class="abs hero-sub">REAL TIME REASONING SOLUTIONS</div>
<div class="abs dots"><i></i><i></i><i></i><i></i></div>

<div class="abs dropdown">
  <ul>
    <li>ALARM MANANGEMENT</li>
    <li>ASSET MANAGEMENT</li>
    <li>PREDICTIVE DISTINCTIVE</li>
    <li>LOGIC DESIGN</li>
  </ul>
  <div class="abs drop-photo" role="img" aria-label="Industrial plant lit at night"></div>
  <div class="abs drop-label">INDUSTRY</div>
</div>

<div class="abs section-title" style="top:529px">INTRODUCTIE KELVORA</div>
<svg class="abs rule" style="top:560px" viewBox="0 0 837 6"><line x1="323" y1="3" x2="515" y2="3" stroke="#bbb" stroke-width="1"/><line x1="323" y1="3" x2="419" y2="3" stroke="#c0391f" stroke-width="1.5"/><circle cx="324" cy="3" r="2.5" fill="#c0391f"/></svg>

<div class="abs intro">
  <p>Companies have invested to get data out of processes. New technologies have been developed to getreal-time data out of the harshest places, like oil-well drill heads or the Great Barrier Riff. Data in itself means nothing without the context the data is collected in. Example: data from equipment under maintenance does not provide information to operations. Information - data which is valid and meaningful - can overwhelm any user without the proper knowledge to interpret this information.</p>
  <p>Kelvora technology enables easy application of such knowledge in a comprehensible – visual – representation and makes hypothetical reasoning with information possible providing meaningful advisories to subscribers when they need it or when it is required that they are made aware of a situation which requires their attention.</p>
</div>

<div class="abs divider"></div>

<div class="abs section-title" style="top:740px">OUR CLIENTS</div>
<svg class="abs rule" style="top:770px" viewBox="0 0 837 6"><line x1="351" y1="3" x2="487" y2="3" stroke="#bbb" stroke-width="1"/><line x1="351" y1="3" x2="418" y2="3" stroke="#c0391f" stroke-width="1.5"/><circle cx="352" cy="3" r="2.5" fill="#c0391f"/></svg>

<div class="abs clients">
  <div class="client"><i></i>Norvane</div>
  <div class="client"><i></i>Teskar</div>
  <div class="client">Brouwhal</div>
  <div class="client">Lindqvist</div>
  <div class="client"><i></i>Maritex</div>
  <div class="client">Sabrel</div>
  <div class="client"><i></i>Coralis</div>
</div>

<div class="abs footer"></div>
<div class="abs social"><i aria-label="Social profile"></i><i aria-label="Social profile"></i><i aria-label="Social profile"></i></div>
<div class="abs email">Enter your email address</div>
<div class="abs subscribe">SUBSCRIBE</div>

<div class="abs panel"></div>
<div class="abs col" style="left:95px"><h4>SOLUTIONS</h4><ul><li>KAM Alarm Reporting</li><li>KAM Alarm Analysis</li><li>KAM Alarm Expert</li><li>USE</li></ul></div>
<div class="abs col" style="left:248px"><h4>INDUSTRIES</h4><ul><li>Industry</li><li>Telecom</li><li>Power</li><li>Utilities</li><li>Infra</li></ul></div>
<div class="abs col" style="left:379px"><h4>ABOUT US</h4><ul><li>Company</li><li>Overview</li><li>Leadership</li><li>Partners</li><li>Locations</li></ul></div>
<div class="abs col" style="left:508px"><h4>NEWS</h4><ul><li>Product News</li><li>Partner News</li><li>Events</li><li>Press Releases</li><li>Vacancies</li></ul></div>
<div class="abs col" style="left:623px"><h4>CONTACT DETALS</h4></div>
<svg class="abs" style="left:622px;top:1041px" width="11" height="14" viewBox="0 0 11 14"><path d="M5.5 0A5 5 0 0 1 10.5 5c0 4-5 9-5 9S.5 9 .5 5A5 5 0 0 1 5.5 0z" fill="#fff"/><circle cx="5.5" cy="5" r="1.8" fill="#232122"/></svg>
<div class="abs contact" style="left:641px;top:1035px">Company Inc., 14 Harlow Street Albany, NY 122, USA</div>
<svg class="abs" style="left:621px;top:1101px" width="8" height="14" viewBox="0 0 8 14"><path d="M6 1C2 2 1 5 1 7s1 5 5 6" stroke="#fff" stroke-width="2.2" fill="none" stroke-linecap="round"/></svg>
<div class="abs contact" style="left:640px;top:1098px">+31 (0) 20 555 0148</div>

<div class="abs copy">Copyright @ 2015 Kelvora.All Rights Reserved.</div>

</body>
</html>
```